Consulting company needs Business Cards - rough concept provided

I'm looking for someone to take our business card idea and make is slick and polished - to communicate our high-end, sophisticated, serious consulting business. We have a rough layout we did in-house. We are open to ideas on repo-ing elements, adjusting sizes, typefaces etc... within the general concept we've already come up with. We want it to be super-clean and sophisticated. We want to keep the white backgrounds, and blue brand colors. Our goal is to print with painted blue edges on thick cardstock. Thank you!!

```html
<!DOCTYPE html>
<html lang="en">
<head>
<meta charset="utf-8">
<title>Halvern Business Card</title>
<link href="https://fonts.googleapis.com/css2?family=Figtree:wght@300;400;500;700;800&display=swap" rel="stylesheet">
<style>
  :root {
    --brand-blue: #009cdc;
    --light-blue: #45b6e6;
    --page-bg: #ecf1f8;
    --edge-grey: #bcbdbf;
    --paper: #ffffff;
    --ink: #111111;
  }
  * { box-sizing: border-box; margin: 0; padding: 0; }
  html, body {
    width: 1200px; height: 1000px; overflow: hidden;
    background: var(--page-bg);
    font-family: "Figtree", sans-serif;
  }
  .stage { position: relative; width: 1200px; height: 1000px; }
  .card {
    position: absolute; left: 296px; width: 608px; height: 353px;
    background: var(--edge-grey);
    box-shadow: 4px 8px 14px rgba(60, 70, 90, 0.18);
  }
  .card--front { top: 120px; }
  .card--back { top: 527px; }
  .card__face {
    position: absolute; left: 11px; top: 11px; width: 586px; height: 331px;
    background: var(--paper); overflow: hidden;
  }
  .accent-bar { position: absolute; width: 103px; height: 15px; background: var(--brand-blue); }
  .accent-bar--bottom-left { left: 0; bottom: 0; }
  .accent-bar--top-right { right: 0; top: 0; }

  .brand-panel {
    position: absolute; left: 209px; top: 0; right: 0; bottom: 0;
    background: var(--brand-blue);
  }
  .brand-name {
    position: absolute; right: 27px; top: 14px;
    font-weight: 800; font-size: 66px; letter-spacing: 0;
    color: var(--paper); line-height: 1; white-space: nowrap;
  }
  .person { position: absolute; left: 31px; top: 150px; }
  .person__marker { display: block; margin-left: 31px; margin-bottom: 6px; }
  .person__first { font-weight: 400; font-size: 30px; line-height: 0.85; color: var(--ink); }
  .person__last { font-weight: 800; font-size: 29px; line-height: 0.95; color: var(--ink); letter-spacing: -0.3px; }
  .person__role { font-weight: 300; font-size: 14.5px; color: var(--light-blue); margin-top: 1px; letter-spacing: 0.1px; }

  .contact {
    position: absolute; left: 375px; top: 224px;
    border-left: 4px solid var(--edge-grey);
    padding-left: 11px; height: 89px;
    color: var(--paper); font-size: 13.5px; font-weight: 400; line-height: 17px;
    white-space: nowrap;
  }
  .contact__address { margin-top: 2px; }
  .contact__line { margin-top: 5px; }

  .value-list { position: absolute; left: 70px; top: 49px; list-style: none; }
  .value-list__item {
    display: flex; align-items: center; height: 58px;
    font-size: 24px; color: var(--ink); font-weight: 400; white-space: nowrap;
  }
  .value-list__item svg { margin-right: 13px; flex: none; }
  .value-list__lead { color: var(--brand-blue); font-weight: 700; margin-right: 7px; }
</style>
</head>
<body>
<main class="stage">
  <section class="card card--front">
    <div class="card__face">
      <div class="brand-panel"></div>
      <div class="brand-name">HALVERN</div>
      <div class="person">
        <svg class="person__marker" width="30" height="22" viewBox="0 0 30 22" aria-hidden="true">
          <polygon points="0,0 30,0 15,22" fill="var(--brand-blue)"/>
        </svg>
        <p class="person__first">JORDAN</p>
        <p class="person__last">ELLERY</p>
        <p class="person__role">BRAND CONSULTANT</p>
      </div>
      <div class="contact">
        <p class="contact__address">4820 Harbor Ave, Ste 210<br>Lakemont, Ca 91820</p>
        <p class="contact__line">555 214 0376</p>
        <p class="contact__line">jordan@halvern.com</p>
      </div>
      <div class="accent-bar accent-bar--bottom-left"></div>
    </div>
  </section>

  <section class="card card--back">
    <div class="card__face">
      <div class="accent-bar accent-bar--top-right"></div>
      <ul class="value-list">
        <li class="value-list__item"><svg width="17" height="23" viewBox="0 0 17 23" aria-hidden="true"><polygon points="0,0 17,11.5 0,23" fill="var(--brand-blue)"/></svg><span class="value-list__lead">We help</span>[target demographic]</li>
        <li class="value-list__item"><svg width="17" height="23" viewBox="0 0 17 23" aria-hidden="true"><polygon points="0,0 17,11.5 0,23" fill="var(--brand-blue)"/></svg><span class="value-list__lead">Achieve</span>[desired emotional outcome]</li>
        <li class="value-list__item"><svg width="17" height="23" viewBox="0 0 17 23" aria-hidden="true"><polygon points="0,0 17,11.5 0,23" fill="var(--brand-blue)"/></svg><span class="value-list__lead">By</span>[our unique approach]</li>
        <li class="value-list__item"><svg width="17" height="23" viewBox="0 0 17 23" aria-hidden="true"><polygon points="0,0 17,11.5 0,23" fill="var(--brand-blue)"/></svg><span class="value-list__lead">Because</span>[our brand beliefs]</li>
      </ul>
      <div class="accent-bar accent-bar--bottom-left"></div>
    </div>
  </section>
</main>
</body>
</html>
```